「冷凍惣菜」のパッケージ(外装の箱)デザインをお願いします。

惣菜が入ったプラスチックの容器に、外装として筒状の紙をかぶせます。
外装の天面と側面のデザインを作成していただきたいです。

【商品概要】
・家庭では作れない、手間のかかる料理を、レンジで温めるだけで手軽に食べられることがコンセプト
(商品例:牛タンの赤ワイン煮、パエリア、ブイヤベースなど)

・外食の専門店のような本格的な味が特徴

・価格帯は1000円前後、ちょっとしたごちそうメニュー
(一般的な冷凍食品と比べると高いが、お店で食べると2000円以上するものが1000円で食べられるイメージ)

・2~2.5人前、ターゲットは夫婦

・スーパーマーケットで販売します

【パッケージデザインについて】
・洋風を連想させるようなデザイン

・フランス料理やイタリア料理といった洋食の製品向け

・今回募集したデザインを、洋食料理共通のデザインとして使用します。
(例えば、「牛タンの赤ワイン煮」と「パエリア」に同じデザインのパッケージを使用するということ)

・各商品ごとに、商品名と画像のシールをつくり、それぞれパッケージの天面に貼る予定です。そのため、商品名と画像のスペースを考慮したデザインにしていただきたいです。(シールについて詳細は未定)

・他の有名メーカーの冷凍食品にパッケージで負けないような、目立つデザインでお願いします。

ご質問などありましたらお気軽にご連絡ください。
・添付ファイルに、パッケージの写真と実際の大きさを記載しています。
角度もありますので、デザイン作成時には考慮していただきたいです
・なるべく2色でデザインを仕上げていただきたです。
2色ではなく、3色を使用したデザインでも構いません。
念のため、弊社のロゴデータを添付します。お好きなようにデザインに使っていただいても大丈夫です。
ただ、ロゴや会社名はパッケージにいれる必要はありません。
全体的なデザインがイメージと近いものを採用させていただきます。
本製品は、外装(添付写真の白い箱の部分)にデザインを印字したものを共通で使用し、
商品名や画像はシールとして商品ごとに貼ることで販売する予定です。

今回依頼しておりますパッケージでは、
仮で商品名や画像なども入れた、全体としてのパッケージデザインを作成していただきたいです。
商品名は「シーフードパエリア」や「牛タンの赤ワイン煮」など、何でも構いません。
また、商品名や商品画像は別途シールとなるため、この部分の色数は、背景のデザインの色数と別で考えていただければと思います。
商品名と商品画像は1枚のシールで添付できるようにデザインが一体となっているほうが好ましいです。

商品画像については、最終的には実際の商品をお洒落に盛り付けた写真を撮って、
それを添付するイメージです。

本デザイン作成にあたっては、何かお洒落な皿に盛られた料理のサンプル画像等々を
ご使用いただけるとありがたいです。
多くのご提案ありがとうございます。

前回記載させていただいたように
商品名と画像をひとつにしたシールをパッケージに貼る予定です。
シールとなったときに貼りやすい(少し斜めになったり、貼る位置が多少ずれても目立たない等)
がデザインの要素としてあると助かります。

よろしくお願いします。
ご提案ありがとうございます。

2点、追記があります。

① パッケージのサイズについて

申し訳ありませんが、下記のようにパッケージのサイズ変更がございます。
・六角形の筒状から、四角形に変更
・サイズは、たて175㎜×よこ270㎜×高さ52㎜

今後ご提案いただける方は、上記のサイズで作成をお願い致します。

また、既にご提案いただいた方は可能であれば、サイズ調整をしていただけると幸いです。
(募集に関しては、デザインを重視しているため、
今回サイズ調整の時間がとれない方を採用から外す等は行いません)

②デザインについて

パッケージ上面の製品写真(パエリアなど)は大きめにしたデザインが好ましいです。

これまでの依頼内容にも記載させていただいておりますが、
「商品名+製品写真」を1枚のシールにする予定ですので、その旨を考慮したデザインをお願いします。

以上、宜しくお願い致します。

他社にはない、売り場で映えるようなデザインでした。
作業性なども考慮していただけたことが理由です。

数多くのご提案をありがとうございます。
どれもステキなデザインでした。
またの機会がありましたら、宜しくお願い致します。

```html
<!DOCTYPE html>
<html lang="ja">
<head>
<meta charset="utf-8">
<title>冷凍惣菜 パッケージ 天面・側面</title>
<link rel="stylesheet" href="https://fonts.googleapis.com/css2?family=Noto+Serif+JP:wght@400;600;700&family=Cormorant+Garamond:ital,wght@0,500;1,500&display=swap">
<style>
  :root {
    --paper: #ffffff;
    --ink: #161314;
    --wine: #a31e30;
    --wine-deep: #7e1524;
    --cream: #f3ece4;
    --mark: #555;
  }
  html, body {
    margin: 0;
    padding: 0;
    width: 849px;
    height: 1200px;
    overflow: hidden;
    background: var(--paper);
  }
  .sheet {
    position: relative;
    width: 849px;
    height: 1200px;
    font-family: "Noto Serif JP", serif;
  }
  .crop-marks {
    position: absolute;
    inset: 0;
  }
  .panel-top {
    position: absolute;
    left: 62px;
    top: 228px;
    width: 442px;
    height: 748px;
    background: var(--ink);
  }
  .panel-side {
    position: absolute;
    left: 504px;
    top: 228px;
    width: 283px;
    height: 748px;
    background: var(--wine);
  }
  .fold-line {
    position: absolute;
    left: 430px;
    top: 228px;
    width: 1px;
    height: 748px;
    background: rgba(255,255,255,0.12);
  }
  /* product sticker */
  .sticker-photo {
    position: absolute;
    left: 62px;
    top: 468px;
    width: 368px;
    height: 226px;
    background:
      radial-gradient(ellipse 60% 70% at 62% 55%, #6a2a1c 0%, #3b1812 45%, transparent 75%),
      radial-gradient(ellipse 40% 40% at 30% 70%, #8f3a22 0%, transparent 70%),
      linear-gradient(135deg, #2c2523 0%, #4a3a33 45%, #1d1917 100%);
  }
  .sticker-title {
    position: absolute;
    left: 62px;
    top: 486px;
    height: 40px;
    padding: 0 22px 0 14px;
    display: flex;
    align-items: center;
    background: linear-gradient(90deg, var(--wine) 70%, rgba(163,30,48,0));
    color: var(--cream);
    font-size: 24px;
    font-weight: 700;
    letter-spacing: 0.04em;
  }
  .sticker-caption {
    position: absolute;
    left: 182px;
    top: 738px;
    width: 214px;
    height: 28px;
    border: 1px solid rgba(243,236,228,0.55);
    display: flex;
    align-items: center;
    justify-content: center;
    gap: 8px;
    color: var(--cream);
    font-size: 11px;
    letter-spacing: 0.08em;
  }
  .sticker-caption .count {
    width: 18px;
    height: 18px;
    border-radius: 50%;
    background: var(--wine);
    color: var(--cream);
    font-size: 11px;
    display: flex;
    align-items: center;
    justify-content: center;
  }
  /* side panel */
  .brand-ribbon {
    position: absolute;
    left: 598px;
    top: 228px;
    width: 90px;
    height: 268px;
    background: var(--ink);
  }
  .brand-ribbon::before {
    content: "";
    position: absolute;
    inset: 0 8px;
    border-left: 1px solid rgba(243,236,228,0.4);
    border-right: 1px solid rgba(243,236,228,0.4);
  }
  .brand-mark {
    position: absolute;
    left: 0;
    right: 0;
    top: 170px;
    display: flex;
    flex-direction: column;
    align-items: center;
    gap: 6px;
    color: var(--cream);
  }
  .brand-mark .dot {
    width: 24px;
    height: 24px;
    border: 1px solid var(--cream);
    border-radius: 50%;
  }
  .brand-mark .name {
    font-family: "Cormorant Garamond", serif;
    font-size: 11px;
    letter-spacing: 0.08em;
  }
  .tagline {
    position: absolute;
    left: 530px;
    top: 642px;
    width: 240px;
    margin: 0;
    color: var(--cream);
    font-size: 21px;
    font-weight: 600;
    line-height: 1.6;
    letter-spacing: 0.03em;
  }
  .spec-list {
    position: absolute;
    left: 540px;
    top: 746px;
    display: flex;
    gap: 6px;
    margin: 0;
    padding: 0;
    list-style: none;
  }
  .spec-list li {
    height: 24px;
    padding: 0 8px;
    border: 1px solid var(--cream);
    color: var(--cream);
    font-size: 12px;
    display: flex;
    align-items: center;
    letter-spacing: 0.06em;
  }
  .footer-mark {
    position: absolute;
    left: 622px;
    top: 900px;
    width: 42px;
    height: 42px;
    border: 1px solid rgba(243,236,228,0.75);
    border-radius: 50%;
    display: flex;
    align-items: center;
    justify-content: center;
    color: var(--cream);
    font-family: "Cormorant Garamond", serif;
    font-size: 7px;
    letter-spacing: 0.04em;
    text-align: center;
    line-height: 1.1;
  }
</style>
</head>
<body>
<main class="sheet">
  <svg class="crop-marks" width="849" height="1200" viewBox="0 0 849 1200" aria-hidden="true">
    <g stroke="var(--mark)" stroke-width="0.8" fill="none">
      <path d="M62 190 V215 M40 228 H50 M787 190 V215 M799 228 H822"/>
      <path d="M62 989 V1014 M40 976 H50 M787 989 V1014 M799 976 H822"/>
      <path d="M504 190 V215 M504 989 V1014"/>
      <path d="M14 602 H40 M809 602 H835"/>
      <circle cx="27" cy="602" r="6"/><circle cx="822" cy="602" r="6"/>
      <path d="M424 180 V205 M424 999 V1024"/>
    </g>
  </svg>

  <section class="panel-top" aria-label="天面"></section>
  <div class="fold-line"></div>

  <div class="sticker-photo" role="img" aria-label="鉄鍋に盛られた牛タンの赤ワイン煮と人参、ハーブの料理写真"></div>
  <h1 class="sticker-title">牛タンの赤ワイン煮</h1>
  <p class="sticker-caption">牛タンの赤ワイン煮込み <span class="count">5</span></p>

  <section class="panel-side" aria-label="側面"></section>
  <div class="brand-ribbon">
    <div class="brand-mark">
      <span class="dot"></span>
      <span class="name">Table Rouge</span>
    </div>
  </div>
  <p class="tagline">専門店のような本格的な<br>味を気軽にご家庭で。</p>
  <ul class="spec-list">
    <li>要冷凍</li>
    <li>2〜2.5人分</li>
  </ul>
  <div class="footer-mark">Table<br>Rouge</div>
</main>
</body>
</html>
```